Save The Date- Vintage Hawaiian postcard theme

I'm looking for a custom design for the Save the Date for my wedding. I'm getting married in Maui, Hawaii in May, and I'd like a Save the Date that appears like a vintage Hawaiian postcard. I'd also like for it to say:Save the DateKayvon and Imogen are getting marriedMay 10, 2020Maui, Hawaii

```html
<!DOCTYPE html>
<html lang="en">
<head>
<meta charset="utf-8">
<title>Save the Date – Tobias and Imogen</title>
<link rel="stylesheet" href="https://fonts.googleapis.com/css2?family=Montserrat:wght@300;800&display=swap">
<style>
  :root {
    --page-bg: #ffffff;
    --ink: #161616;
    --photo-top: #6cc3dc;
    --photo-mid: #9fdbdc;
    --photo-bottom: #a8d3b0;
    --placeholder-ink: rgba(22, 22, 22, 0.16);
  }
  * { box-sizing: border-box; margin: 0; padding: 0; }
  html, body {
    width: 1200px;
    height: 1200px;
    overflow: hidden;
    background: var(--page-bg);
  }
  .save-the-date-card {
    position: absolute;
    left: 50px;
    top: 292px;
    width: 1100px;
    height: 616px;
    overflow: hidden;
    font-family: "Montserrat", sans-serif;
    color: var(--ink);
  }
  .beach-photo {
    position: absolute;
    inset: 0;
    background: linear-gradient(180deg, var(--photo-top) 0%, var(--photo-mid) 50%, var(--photo-bottom) 100%);
  }
  .headline {
    position: absolute;
    left: 0;
    top: 0;
    width: 1100px;
    height: 260px;
    overflow: visible;
  }
  .headline-text {
    font-family: "Montserrat", sans-serif;
    font-weight: 300;
    font-size: 70px;
    letter-spacing: 1px;
    fill: var(--ink);
  }
  .heart-arrow {
    position: absolute;
    left: 522px;
    top: 176px;
    width: 64px;
    height: 52px;
    background: var(--placeholder-ink);
    border-radius: 8px;
  }
  .couple-names {
    position: absolute;
    left: 0;
    right: 0;
    top: 248px;
    text-align: center;
    font-weight: 800;
    font-size: 45px;
    line-height: 60px;
  }
  .announcement {
    position: absolute;
    left: 0;
    right: 0;
    top: 302px;
    text-align: center;
    font-weight: 300;
    font-size: 45px;
    line-height: 56px;
  }
  .couple-portrait {
    position: absolute;
    left: 465px;
    top: 378px;
    width: 170px;
    height: 124px;
    background: var(--placeholder-ink);
    border-radius: 10px;
  }
  .event-detail {
    position: absolute;
    top: 432px;
    font-weight: 800;
    font-size: 34px;
    line-height: 44px;
    white-space: nowrap;
    transform: translateX(-50%);
  }
  .event-date { left: 327px; }
  .event-place { left: 780px; }
</style>
</head>
<body>
  <main class="save-the-date-card">
    <div class="beach-photo" role="img" aria-label="Aerial photo of a tropical lagoon beach with white sand, turquoise water and palm trees"></div>
    <h1 class="headline">
      <svg class="headline" viewBox="0 0 1100 260" aria-label="Save the date">
        <path id="headline-arc" d="M 300 190 Q 550 110 800 196" fill="none"/>
        <text class="headline-text" text-anchor="middle">
          <textPath href="#headline-arc" startOffset="50%">Save the date</textPath>
        </text>
      </svg>
    </h1>
    <div class="heart-arrow" role="img" aria-label="Small line drawing of a heart pierced by an arrow"></div>
    <h2 class="couple-names">Tobias and Imogen</h2>
    <p class="announcement">are getting married</p>
    <div class="couple-portrait" role="img" aria-label="Line illustration of the bride and groom"></div>
    <p class="event-detail event-date">May 10, 2020</p>
    <p class="event-detail event-place">Maui, Hawaii</p>
  </main>
</body>
</html>
```